A Book Cover For a Book Called "Tamsire"

Attached are two files for the ISBN bar graph for the print version of the cover! Same image, just two different formats.
Updates

Project Deadline Extended Reason: We'd like to see a few more designs, and work with a few of the designs already submitted. Added Tuesday, October 24, 2017

Target Market(s)

young adult female, parents

Colors

Designer to choose colors to be used in the design.

```html
<!DOCTYPE html>
<html lang="en">
<head>
<meta charset="utf-8">
<title>Tamsire — A Memoir</title>
<link rel="stylesheet" href="https://fonts.googleapis.com/css2?family=Della+Respira&family=Old+Standard+TT:wght@400;700&display=swap">
<style>
  :root {
    --page-bg: #ffffff;
    --cover-top: #3f4043;
    --cover-bottom: #050505;
    --title-crimson: #d4134f;
    --byline-blush: #f3e2e4;
    --subtitle-rose: #d8b9bd;
    --photo-light: #c9c3c6;
    --photo-mid: #5b5558;
    --photo-floor: #8a7a3a;
  }
  * { margin: 0; padding: 0; box-sizing: border-box; }
  html, body {
    width: 1200px;
    height: 1000px;
    overflow: hidden;
    background: var(--page-bg);
  }
  .canvas {
    position: relative;
    width: 1200px;
    height: 1000px;
  }
  .book-cover {
    position: absolute;
    left: 330px;
    top: 20px;
    width: 550px;
    height: 960px;
    background: linear-gradient(180deg, var(--cover-top) 0%, #1c1c1e 45%, var(--cover-bottom) 100%);
    overflow: hidden;
  }
  .book-title {
    position: absolute;
    top: 22px;
    left: 0;
    width: 100%;
    text-align: center;
    white-space: nowrap;
    font-family: "Della Respira", serif;
    font-weight: 400;
    font-size: 106px;
    line-height: 1;
    color: var(--title-crimson);
    letter-spacing: -1px;
    transform: scaleY(1.9);
    transform-origin: top center;
  }
  .byline {
    position: absolute;
    top: 318px;
    right: 24px;
    white-space: nowrap;
    font-family: "Old Standard TT", serif;
    font-weight: 700;
    font-size: 27px;
    line-height: 1.2;
    color: var(--byline-blush);
  }
  .byline .co-author {
    display: block;
    padding-left: 92px;
  }
  .cover-photo {
    position: absolute;
    left: 148px;
    top: 380px;
    width: 235px;
    height: 285px;
    background:
      radial-gradient(ellipse 40% 20% at 50% 82%, var(--photo-floor) 0%, rgba(138,122,58,0) 100%),
      radial-gradient(ellipse 45% 55% at 50% 45%, var(--photo-light) 0%, var(--photo-mid) 45%, rgba(10,10,10,0) 100%);
  }
  .subtitle {
    position: absolute;
    bottom: 36px;
    left: 0;
    width: 100%;
    text-align: center;
    white-space: nowrap;
    font-family: "Old Standard TT", serif;
    font-weight: 400;
    font-size: 70px;
    letter-spacing: 1px;
    color: var(--subtitle-rose);
  }
</style>
</head>
<body>
  <div class="canvas">
    <section class="book-cover">
      <h1 class="book-title">TAMSIRE</h1>
      <p class="byline">by Lena Marlow<span class="co-author">with Clara Quinn</span></p>
      <div class="cover-photo" role="img" aria-label="Photograph of a ballet dancer's feet en pointe in satin shoes under a spotlight on a wooden floor"></div>
      <p class="subtitle">A MEMOIR</p>
    </section>
  </div>
</body>
</html>
```